Design website home page for pathology consulting company

Starting a new consulting company with anatomic pathologists focused on expert diagnosis and second opinions on difficult pathology cases. In the near future we will be incorporating next generation diagnostics for rare diseases of childhood into the business. These include discovery and testing of DNA for mutations.

The company is formed around one of the best known pathologists in the world named Marcus "Buddy" Halvorsen. The name of the company is "BuddyScope"

We had a logo design by Sketchfold - it is great. I will attach file as soon as I have it (contest ending today). Our company is medical, uses microscopes, DNA, probably will focus on childhood diseases but not solely on childhood diseases. we're not particularly conservative, but the customers we want to appeal to include older practicing pathologists as well as patients (sometimes parents) looking for second opinions.

Think a group of expert doctors diagnosing disease through the microscope and through DNA technology, ages ranging from 35-75 all trained by the best pathologist in the world - "Buddy"

We receive glass slides from diseases from patients all over the world from docs who need an expert to tell them what is the diagnosis. So "path to the diagnosis" is also part of the company marketing message.

We want the website design to describe our company but be very simple to find what one is looking for as we will use it as the launch page to:
1) order services
2) check results/reports
3) set up new account
4) speak with one of the pathologists
5) see our test menu
6) access our educational material/webinars

Update - looking for home page design and then finalists will ask for second page design to keep with theme - ok?

Reason: realized this project isn't web design but web home page design - thanks

Reason: Holidays for some in next two weeks

Reason: Hot discussion among collaborators for a few of the submissions. Will provide detail individually this weekend. Thanks so much for all the submissions!

Target Market(s)

Referring pathologists, physicians who want second opinions on pathology disease diagnosis, patients who have had biopsies (either patients themselves or parents of patients), generally high education level

Industry/Entity Type

Marketing

Requirements
Must have
• BuddyScope
Next Generation Pathology Consultants

```html
<!DOCTYPE html>
<html lang="en">
<head>
<meta charset="utf-8">
<title>BuddyScope – Next Generation Pathology Consultants</title>
<link href="https://fonts.googleapis.com/css2?family=Libre+Baskerville:wght@400;700&family=Roboto:wght@300;400;500&family=Roboto+Condensed:wght@400;700&display=swap" rel="stylesheet">
<style>
  :root{
    --page-bg:#ececec;
    --panel:#ffffff;
    --brand-blue:#0d56a6;
    --brand-blue-dark:#084a8f;
    --icon-grad-top:#1a7fd0;
    --icon-grad-bottom:#0a4f9c;
    --text:#4a4a4a;
    --nav-text:#5a5a5a;
    --caption-bg:rgba(40,40,40,.82);
    --footer-bg:#9b9b9b;
    --footer-text:#ffffff;
    --rule:#d4d4d4;
  }
  *{box-sizing:border-box;margin:0;padding:0}
  html,body{width:1064px;height:1200px;overflow:hidden}
  body{
    background:linear-gradient(100deg,#f4f4f4 0%,#e6e6e6 40%,#efefef 60%,#e3e3e3 100%);
    font-family:"Roboto",Arial,sans-serif;color:var(--text);
  }
  .site{position:absolute;left:133px;top:0;width:798px;height:1200px;background:var(--panel);box-shadow:0 0 6px rgba(0,0,0,.18)}

  /* header */
  .site-header{position:relative;height:91px;background:linear-gradient(#ffffff,#f3f3f3);border-bottom:1px solid var(--rule)}
  .brand{position:absolute;left:13px;top:10px;display:flex;flex-direction:column;align-items:center;width:112px}
  .brand-mark{width:52px;height:52px;border-radius:50%;background:#c9c9c9}
  .brand-name{margin-top:4px;font-family:"Libre Baskerville",Georgia,serif;font-size:14px;color:var(--brand-blue);letter-spacing:.3px}
  .brand-tag{font-size:5.6px;color:#666;white-space:nowrap}
  .search{position:absolute;left:612px;top:12px;width:174px;height:25px;border:1px solid #aaa;background:#fff}
  .search svg{position:absolute;right:7px;top:5px}
  .main-nav{position:absolute;right:13px;top:54px;display:flex;gap:31px;font-size:11.8px;color:var(--nav-text)}

  /* hero */
  .hero{position:relative;height:408px;background:linear-gradient(90deg,#f2f4f6 0%,#e8ebee 35%,#d9dee4 55%,#5c85c9 72%,#2a5fb8 100%)}
  .hero-caption{position:absolute;left:0;right:0;bottom:0;height:41px;background:var(--caption-bg);display:flex;align-items:center;color:#fff}
  .hero-caption p{position:absolute;left:113px;font-family:"Roboto Condensed",Arial,sans-serif;font-size:15.5px}
  .hero-caption strong{font-weight:700}
  .learn-more{position:absolute;left:596px;top:10px;width:97px;height:23px;background:var(--brand-blue);color:#fff;font-family:"Libre Baskerville",Georgia,serif;font-weight:700;font-size:8.5px;display:flex;align-items:center;justify-content:center;letter-spacing:.2px}
  .arrow{position:absolute;top:14px}
  .arrow.prev{left:13px}.arrow.next{right:13px}

  /* welcome */
  .welcome{height:270px;padding:38px 13px 0 12px}
  .welcome h1{font-family:"Libre Baskerville",Georgia,serif;font-size:19.5px;font-weight:700;color:var(--brand-blue);letter-spacing:.1px}
  .welcome h1 span{font-weight:400}
  .welcome p{font-size:11.6px;font-weight:300;line-height:17.5px;margin-top:12px;color:#444}
  .welcome p+p{margin-top:17px}

  /* services */
  .services{position:relative;height:322px;background:linear-gradient(#ececec 0,#fff 34px);border-top:1px solid var(--rule);box-shadow:inset 0 2px 3px rgba(0,0,0,.06)}
  .service{position:absolute;width:380px;display:flex;gap:9px}
  .service-icon{flex:none;width:66px;height:66px;border-radius:50%;background:linear-gradient(var(--icon-grad-top),var(--icon-grad-bottom));display:flex;align-items:center;justify-content:center}
  .service h2{margin-top:6px;font-family:"Libre Baskerville",Georgia,serif;font-size:12.5px;font-weight:700;color:var(--brand-blue)}
  .service p{margin-top:5px;font-size:10px;line-height:14px;color:#444}

  /* footer */
  .site-footer{position:absolute;left:0;right:0;bottom:0;height:109px;background:var(--footer-bg);color:var(--footer-text);font-family:"Roboto Condensed",Arial,sans-serif}
  .footer-row{position:absolute;left:16px;display:flex;align-items:center;gap:8px;font-size:10px;white-space:nowrap}
  .footer-row.links{top:22px;font-weight:700}
  .footer-row.contact{top:42px;font-weight:700}
  .footer-row.legal{top:63px;font-weight:400}
  .social{display:flex;gap:3px}
  .social span{width:13px;height:13px;background:#e8e8e8}
  .footer-brand{position:absolute;right:17px;top:17px;display:flex;flex-direction:column;align-items:center;width:112px}
  .footer-brand .brand-mark{width:54px;height:54px;background:#b8b8b8}
  .footer-brand .brand-name{color:#e4e4e4;font-size:14px}
  .footer-brand .brand-tag{color:#e4e4e4}
</style>
</head>
<body>
<div class="site">
  <header class="site-header">
    <div class="brand">
      <div class="brand-mark"></div>
      <div class="brand-name">BuddyScope</div>
      <div class="brand-tag">Next Generation Pathology Consultants</div>
    </div>
    <div class="search">
      <svg width="14" height="14" viewBox="0 0 14 14"><circle cx="5.5" cy="5.5" r="4.3" fill="none" stroke="#555" stroke-width="1.6"/><line x1="8.6" y1="8.6" x2="13" y2="13" stroke="#555" stroke-width="1.8"/></svg>
    </div>
    <nav class="main-nav">
      <span>Company</span><span>Services</span><span>Our Physicians</span><span>Learning Center</span><span>News</span><span>Contact Us</span>
    </nav>
  </header>

  <section class="hero" role="img" aria-label="Photo of a senior pathologist in a white lab coat in a bright laboratory">
    <div class="hero-caption">
      <svg class="arrow prev" width="10" height="14" viewBox="0 0 10 14"><polyline points="8,1 2,7 8,13" fill="none" stroke="#bbb" stroke-width="2.4"/></svg>
      <p><strong>Marcus "Buddy" Halvorsen:</strong> Lorem ipsum dolor sit amet, consectetur adipiscing</p>
      <span class="learn-more">LEARN MORE</span>
      <svg class="arrow next" width="10" height="14" viewBox="0 0 10 14"><polyline points="2,1 8,7 2,13" fill="none" stroke="#bbb" stroke-width="2.4"/></svg>
    </div>
  </section>

  <section class="welcome">
    <h1>WECLOME TO BUDDYSCOPE - <span>Next Generation Pathology Consultants</span></h1>
    <p>Lorem ipsum dolor sit amet, consectetur adipiscing elit. Morbi consectetur venenatis velit quis accumsan. Sed gravida, lectus et mattis scelerisque, neque lacus vehicula lacus, a pellentesque justo erat vitae lacus. Etiam quis purus ultrices, accumsan purus quis, fermentum nunc. Ut sollicitudin eu nisi eu vehicula. Integer fermentum libero vel massa pharetra eleifend in et ante. Nunc quis est justo. Praesent augue nibh, dictum sagittis porta ac, gravida tempor quam. Nullam rhoncus, lacus et rhoncus cursus, lorem sapien lobortis lectus, sit amet tincidunt magna arcu posuere nunc.</p>
    <p>Sed hendrerit tempus est id sollicitudin. Nunc a neque auctor, sodales felis vel, viverra arcu. Curabitur euismod pellentesque luctus. Ut et laoreet felis, in ultrices ligula. Vestibulum euismod elementum felis, ut varius magna tincidunt sit amet. Vivamus luctus id odio id mattis. Morbi sem leo, cursus in condimentum in, iaculis vel massa. Pellentesque euismod mollis purus ac auctor. In sed quam sed felis dictum vestibulum. Vestibulum ornare sodales sapien sit amet pulvinar. Nulla scelerisque turpis sit amet ipsum imperdiet, eget sagittis magna varius. Nam pharetra lorem id risus eleifend, at.</p>
  </section>

  <section class="services">
    <div class="service" style="left:12px;top:47px">
      <div class="service-icon"><svg width="30" height="30" viewBox="0 0 30 30"><g fill="#fff"><circle cx="15" cy="15" r="9"/><g id="teeth"><rect x="12.5" y="2" width="5" height="6"/><rect x="12.5" y="22" width="5" height="6"/><rect x="2" y="12.5" width="6" height="5"/><rect x="22" y="12.5" width="6" height="5"/></g><g transform="rotate(45 15 15)"><rect x="12.5" y="2" width="5" height="6"/><rect x="12.5" y="22" width="5" height="6"/><rect x="2" y="12.5" width="6" height="5"/><rect x="22" y="12.5" width="6" height="5"/></g></g><circle cx="15" cy="15" r="3.6" fill="#1466b8"/></svg></div>
      <div><h2>ORDER SERVICES</h2><p>Lorem ipsum dolor sit amet, consectetur adipiscing elit. Nam porta faucibus vulputate. Sed sit amet vulputate leo ulla bibendum justo.</p></div>
    </div>
    <div class="service" style="left:416px;top:47px">
      <div class="service-icon"><svg width="28" height="32" viewBox="0 0 28 32"><path d="M3 2h15l7 7v21H3z" fill="#fff"/><path d="M18 2v7h7" fill="#cfe2f5"/><g stroke="#1466b8" stroke-width="2"><line x1="8" y1="14" x2="20" y2="14"/><line x1="8" y1="19" x2="20" y2="19"/><line x1="8" y1="24" x2="20" y2="24"/></g></svg></div>
      <div><h2>CHECK RESULTS/REPORTS</h2><p>Curabitur vel tortor pulvinar, vestibulum ligula ut, rutrum nunc. Duis et vehicula mi. Etiam eu rutrum orci nullam vulputate dui ac erat.</p></div>
    </div>
    <div class="service" style="left:12px;top:130px">
      <div class="service-icon"><svg width="26" height="30" viewBox="0 0 26 30"><path d="M7 13V8a6 6 0 0 1 12 0v5" fill="none" stroke="#fff" stroke-width="3"/><rect x="2" y="13" width="22" height="16" rx="2" fill="#fff"/><circle cx="13" cy="20" r="2.6" fill="#1466b8"/><rect x="11.8" y="20" width="2.4" height="5" fill="#1466b8"/></svg></div>
      <div><h2>SET UP NEW ACCOUNT</h2><p>Morbi ut hendrerit magna. Praesent porta nisl at laoreet dapibus. Suspendisse elementum tincidunt lacus, id pulvinar eros.</p></div>
    </div>
    <div class="service" style="left:416px;top:130px">
      <div class="service-icon"><svg width="38" height="28" viewBox="0 0 38 28"><g fill="#fff"><circle cx="24" cy="8" r="6"/><path d="M14 27c0-7 4-11 10-11s10 4 10 11z"/><circle cx="14" cy="10" r="6"/><path d="M3 27c0-7 4-10 11-10s11 3 11 10z"/></g></svg></div>
      <div><h2>SPEAK WITH PATHOLOGISTS</h2><p>Curabitur at venenatis nibh. Nam purus ipsum, ultricies eu eros nec, pretium fringilla tortor. Nunc nec semper arcu estibulum ante.</p></div>
    </div>
    <div class="service" style="left:12px;top:213px">
      <div class="service-icon"><svg width="30" height="28" viewBox="0 0 30 28"><g fill="#fff"><rect x="0" y="0" width="9" height="8"/><rect x="12" y="1" width="18" height="2.6"/><rect x="12" y="5" width="18" height="2.6"/><rect x="0" y="10" width="9" height="8"/><rect x="12" y="11" width="18" height="2.6"/><rect x="12" y="15" width="18" height="2.6"/><rect x="0" y="20" width="9" height="8"/><rect x="12" y="21" width="18" height="2.6"/><rect x="12" y="25" width="18" height="2.6"/></g></svg></div>
      <div><h2>SEE THE TEST MENU</h2><p>Nunc augue nibh, mollis eu bibendum non, dapibus sit amet orci. Praesent ut lorem a ipsum tincidunt congue aliquam luctus lorem.</p></div>
    </div>
    <div class="service" style="left:416px;top:213px">
      <div class="service-icon"><svg width="32" height="32" viewBox="0 0 32 32"><path d="M16 4H6a3 3 0 0 0-3 3v19a3 3 0 0 0 3 3h19a3 3 0 0 0 3-3V16" fill="none" stroke="#fff" stroke-width="3"/><path d="M25 3l4 4-13 13-5 1 1-5z" fill="#fff"/></svg></div>
      <div><h2>ACCESS LEARNING CENTER</h2><p>Morbi dictum vestibulum odio, eu molestie felis mollis non. Donec mattis risus at est cursus, nec vehicula leo tincidunt vestibulum.</p></div>
    </div>
  </section>

  <footer class="site-footer">
    <div class="footer-row links"><span>Home</span>|<span>Company</span>|<span>Services</span>|<span>Our Physicians</span>|<span>Learning Center</span>|<span>News</span>|<span>Contact Us</span>|<span>Site Map</span></div>
    <div class="footer-row contact"><span class="social"><span></span><span></span><span></span><span></span></span>|<span>214 Larkmoor Ave. Brookfield, NY 10488</span>|<span>ph: 555.018.2460</span>|<span>info@BuddyScope.com</span></div>
    <div class="footer-row legal"><span>Privacy Policy</span>|<span>Terms &amp; Conditions</span>|<span>©2013 BuddyScope. All rights reserved.</span></div>
    <div class="footer-brand">
      <div class="brand-mark"></div>
      <div class="brand-name">BuddyScope</div>
      <div class="brand-tag">Next Generation Pathology Consultants</div>
    </div>
  </footer>
</div>
</body>
</html>
```